Alberta, Canada based Environmental Oilfield Consultant need a Business Card Design

We need a business card design for a year old company based in Edmonton, Alberta, Canada called Ferncrest Consulting Inc. We are environmental consultants primarily for oilfield based companies (pipeline cleanup, site consultations, environmental site training, and site evaluations).

We like the color blue or green, something very clean and crisp looking.
We don't really care if there is an otter on it but most of our work is land based and nothing really to do with oceans or larger bodies of water.

The name Ferncrest was the name of our fathers boat, and named our company that in his memory.

```html
<!DOCTYPE html>
<html lang="en">
<head>
<meta charset="utf-8">
<title>Ferncrest Consulting Inc. — Business Card</title>
<link rel="stylesheet" href="https://fonts.googleapis.com/css2?family=Open+Sans:wght@400;600;700&display=swap">
<style>
  :root {
    --page-bg: #dcdcdc;
    --card-bg: #ffffff;
    --panel-bg: #ebebec;
    --panel-rule: #ffffff;
    --brand-green: #8cbf26;
    --ink: #2b2b2b;
    --ink-soft: #555555;
    --rule-dark: #9a9a9a;
  }
  * { box-sizing: border-box; margin: 0; padding: 0; }
  html, body {
    width: 1200px; height: 1000px; overflow: hidden;
    background: var(--page-bg);
    font-family: "Open Sans", Arial, sans-serif;
    color: var(--ink);
  }
  .card {
    position: absolute;
    width: 620px; height: 354px;
    background: var(--card-bg);
  }
  .card--back { left: 120px; top: 110px; }
  .card--front { left: 460px; top: 536px; }

  /* Brand name */
  .brand { color: var(--brand-green); font-weight: 600; line-height: 1; }
  .brand__name { display: block; }
  .brand__suffix { display: block; letter-spacing: 0.18em; }

  /* Front */
  .card--front .brand {
    position: absolute; left: 50%; top: 50%;
    transform: translate(-50%, -50%);
  }
  .card--front .brand__name { font-size: 40px; }
  .card--front .brand__suffix { font-size: 15px; margin-top: 4px; }

  /* Back */
  .panel {
    position: absolute; inset: 18px;
    background: var(--panel-bg);
    border-radius: 22px;
    display: grid;
    grid-template-rows: 56% 44%;
    overflow: hidden;
  }
  .panel__top {
    display: grid; grid-template-columns: 33% 67%;
    border-bottom: 2px solid var(--panel-rule);
  }
  .panel__logo {
    border-right: 2px solid var(--panel-rule);
    display: flex; align-items: flex-end;
    padding: 0 0 34px 22px;
  }
  .panel__logo .brand__name { font-size: 26px; }
  .panel__logo .brand__suffix { font-size: 10px; margin-top: 3px; }
  .services {
    display: grid; grid-template-columns: 1fr 1fr;
    padding: 36px 18px 0 36px;
    list-style: none;
    font-size: 11px; color: var(--ink-soft);
    align-content: start; row-gap: 12px;
  }
  .services li::before {
    content: ""; display: inline-block;
    width: 4px; height: 4px; border-radius: 50%;
    background: var(--ink); margin-right: 10px; vertical-align: middle;
  }
  .panel__bottom {
    display: grid; grid-template-columns: 34% 1px 1fr;
    align-items: center;
  }
  .person { padding-left: 62px; font-size: 12px; }
  .person__name { font-weight: 700; font-size: 13px; color: var(--ink); }
  .person__role, .person__company { color: var(--ink-soft); margin-top: 12px; }
  .divider { width: 1px; height: 118px; background: var(--rule-dark); }
  .contacts {
    list-style: none; padding-left: 28px;
    font-size: 10.5px; color: var(--ink-soft);
    display: grid; row-gap: 12px;
  }
  .contacts li { display: flex; align-items: center; gap: 12px; }
  .contacts svg { width: 12px; height: 12px; fill: var(--ink); flex: none; }
</style>
</head>
<body>

<section class="card card--back" aria-label="Business card back">
  <div class="panel">
    <div class="panel__top">
      <div class="panel__logo">
        <div class="brand">
          <span class="brand__name">Ferncrest</span>
          <span class="brand__suffix">Consulting Inc.</span>
        </div>
      </div>
      <ul class="services">
        <li>Pipeline cleanup</li>
        <li>Environmental site training</li>
        <li>Site consultations</li>
        <li>Site Evaluations</li>
      </ul>
    </div>
    <div class="panel__bottom">
      <div class="person">
        <div class="person__name">Your Name</div>
        <div class="person__role">CEO</div>
        <div class="person__company">Ferncrest</div>
      </div>
      <div class="divider"></div>
      <ul class="contacts">
        <li>
          <svg viewBox="0 0 12 12" aria-hidden="true"><path d="M6 0a4 4 0 0 0-4 4c0 3 4 8 4 8s4-5 4-8a4 4 0 0 0-4-4zm0 5.6A1.6 1.6 0 1 1 6 2.4a1.6 1.6 0 0 1 0 3.2z"/></svg>
          Office 14, 52 Edmonton, Alberta, Canada, T5J 2R4
        </li>
        <li>
          <svg viewBox="0 0 12 12" aria-hidden="true"><path d="M2.4 0.5l2 2.2-1 1.4c.7 1.6 2 2.9 3.6 3.6l1.4-1 2.2 2-1 2.3C5 10.5 1.5 7 .5 1.5z"/></svg>
          +1 780 555 0142
        </li>
        <li>
          <svg viewBox="0 0 12 12" aria-hidden="true"><path d="M0 2h12v1L6 7 0 3zM0 4.3l6 4 6-4V10H0z"/></svg>
          name@ferncrest.com
        </li>
        <li>
          <svg viewBox="0 0 12 12" aria-hidden="true"><path d="M6 0a6 6 0 1 0 0 12A6 6 0 0 0 6 0zm4.8 5.3H8.7a9 9 0 0 0-.8-3.7 4.9 4.9 0 0 1 2.9 3.7zM6 1.2c.6.8 1.1 2.3 1.2 4.1H4.8C4.9 3.5 5.4 2 6 1.2zM4.1 1.6a9 9 0 0 0-.8 3.7H1.2a4.9 4.9 0 0 1 2.9-3.7zM1.2 6.7h2.1a9 9 0 0 0 .8 3.7 4.9 4.9 0 0 1-2.9-3.7zM6 10.8c-.6-.8-1.1-2.3-1.2-4.1h2.4c-.1 1.8-.6 3.3-1.2 4.1zm1.9-.4a9 9 0 0 0 .8-3.7h2.1a4.9 4.9 0 0 1-2.9 3.7z"/></svg>
          www.ferncrest.com
        </li>
      </ul>
    </div>
  </div>
</section>

<section class="card card--front" aria-label="Business card front">
  <div class="brand">
    <span class="brand__name">Ferncrest</span>
    <span class="brand__suffix">Consulting Inc.</span>
  </div>
</section>

</body>
</html>
```